Property Finance Company - Orin Ventures Limited

Background: Orin Ventures Group Limited is a private property finance company. Orin Ventures Group has capital to directly fund first mortgage, mezzanine and preferred equity financing. We also acquire performing, sub-performing and distressed debt.

Orin Ventures' management philosophy emphasises expertise, innovation, wisdom, honesty and competitiveness. Orin Ventures are not finance brokers - we provide debt funding to the commercial property and residential development sectors. Our process is built from experience and cumutavely Orin Ventures' Directors have in excess of 60 years wisdom.

The aim of the website will be to increase brand awareness, provide clients with comfort around our level of skill and background on who we are, generate more sales, and provide examples of projects that we have funded.

The website is a new product launch, and we need to use our Orin Ventures logo that has just been designed. We like a dark background, and either black/silver/grey/ jade green, or black/gold/jade green colours.

Our unique advantages are that we have fast turnaround times, we can solve clients funding problems and we know what we are doing. Our target audience will be viewing the website on both desktop and mobile devices.

We would like to have the following pages:

Home
About
Team
Services
Project Experience
Contact

Competitors Website: http://www.tarvelo.com/

We would also like to have the option of video footage in our website, as you can see in our competitors website.

Overall we want a really slick, elegant but modern website that is better than www.tarvelo.com

Target Market(s)

Finance borrowers, property developers, accountants, lawyers, businesspeople, high net worth people

Industry/Entity Type

Finance

Requirements
Must have
• Please see project description
Nice to have
Should not have

```html
<!DOCTYPE html>
<html lang="en">
<head>
<meta charset="utf-8">
<title>Orin Ventures Group</title>
<link href="https://fonts.googleapis.com/css2?family=Open+Sans:wght@400;600;700&display=swap" rel="stylesheet">
<style>
:root{
  --black:#0b0b0b;
  --dark:#161616;
  --panel:#1c1c1c;
  --gold:#e8b21c;
  --gold-deep:#c8920c;
  --green:#1d8a47;
  --green-deep:#146c36;
  --text-light:#d6d6d6;
  --text-muted:#9a9a9a;
  --text-dark:#444;
  --white:#fff;
  --light-bg:#e4e4e4;
}
*{box-sizing:border-box;margin:0;padding:0}
html,body{width:750px;height:1200px;overflow:hidden}
body{position:relative;background:var(--black);font-family:"Open Sans",Arial,sans-serif;color:var(--text-light)}
.site-header{position:absolute;top:0;left:0;width:750px;height:70px;background:var(--black)}
.brand{position:absolute;left:105px;top:22px;display:flex;align-items:center;gap:8px;color:var(--white);font-weight:700;font-size:13px;letter-spacing:.5px}
.brand-mark{width:22px;height:22px;border-radius:50%;background:var(--gold)}
.header-phone{position:absolute;left:495px;top:12px;font-size:11px;color:var(--white);display:flex;align-items:center;gap:5px}
.main-nav{position:absolute;left:350px;top:40px;display:flex;gap:16px;font-size:9px;font-weight:600;color:var(--white)}
.main-nav .active{color:var(--gold)}
.hero{position:absolute;top:70px;left:0;width:750px;height:280px;background:linear-gradient(180deg,#1d3f78 0%,#3b6aa6 35%,#8a7a68 70%,#3a3028 100%)}
.watch-btn{position:absolute;left:110px;top:252px;display:flex;align-items:center;gap:5px;border:1px solid var(--white);border-radius:12px;padding:3px 10px 3px 4px;font-size:8px;color:var(--white);background:rgba(0,0,0,.35)}
.gold-rule{position:absolute;left:0;width:750px;height:4px;background:var(--gold)}
.services-band{position:absolute;top:354px;left:0;width:750px;height:160px;background:var(--black)}
.service-card{position:absolute;top:46px;width:166px;height:100px;background:var(--green);border:1px solid var(--green-deep);padding:8px 0 0 10px}
.service-card h3{font-size:11px;font-weight:700;color:var(--gold)}
.service-card h3 span{color:var(--white);font-weight:600}
.service-card p{width:76px;font-size:7px;line-height:1.35;color:#e6f2ea;margin-top:4px}
.btn{display:inline-block;background:var(--gold);color:#222;font-size:7px;font-weight:700;padding:3px 9px;border-radius:10px;margin-top:6px}
.service-photo{position:absolute;right:6px;top:16px;width:66px;height:66px;border-radius:50%;border:3px solid var(--gold)}
.welcome{position:absolute;top:514px;left:0;width:750px;height:262px;background:var(--dark)}
.welcome-emblem{position:absolute;left:105px;top:42px;width:150px;height:150px;border-radius:50%;background:#2a2a2a}
.welcome h2{position:absolute;left:275px;top:42px;font-size:19px;font-weight:400;color:var(--white)}
.welcome h2 span{color:var(--gold);font-weight:600}
.welcome-copy{position:absolute;left:275px;top:80px;width:370px;font-size:8.5px;line-height:1.6;color:var(--text-muted)}
.welcome-copy p+p{margin-top:10px}
.welcome .btn{position:absolute;left:275px;top:196px}
.highlights{position:absolute;top:776px;left:0;width:750px;height:236px;background:linear-gradient(180deg,#cfcfcf,#efefef)}
.info-card{position:absolute;top:24px;height:192px;background:var(--white);border:1px solid #d0d0d0;padding:10px 12px;color:var(--text-dark)}
.info-card h3{font-size:13px;font-weight:600;color:#555;margin-bottom:8px}
.info-card h3 span{color:var(--gold-deep)}
.why-card{left:105px;width:270px}
.why-list{list-style:none;font-size:8px;line-height:2}
.why-list li{display:flex;align-items:center;gap:5px}
.why-photo{position:absolute;right:0;bottom:0;width:120px;height:170px;background:linear-gradient(180deg,#d9d3c8,#5a84b4)}
.testimonial-card{left:383px;width:262px}
.quote{width:130px;font-size:8px;line-height:1.55;color:#666;position:relative;padding-left:12px}
.quote::before{content:"\201C";position:absolute;left:0;top:-4px;font-size:18px;color:var(--gold)}
.quote-name{margin:8px 0 0 12px;font-size:9px;font-weight:700;color:#333}
.customer-photo{position:absolute;right:0;bottom:0;width:110px;height:170px;background:linear-gradient(180deg,#e6e2dc,#c9b8a6)}
.dots{position:absolute;left:24px;bottom:12px;display:flex;gap:4px}
.dots i{width:6px;height:6px;border-radius:50%;background:#bbb}
.dots i:first-child{background:#555}
.site-footer{position:absolute;top:1016px;left:0;width:750px;height:184px;background:var(--black)}
.footer-col{position:absolute;top:28px;font-size:8px;line-height:1.6;color:var(--text-muted)}
.footer-col h4{font-size:10px;font-weight:600;color:var(--white);margin-bottom:8px}
.news-col{left:105px}
.news-form{display:flex;width:150px}
.news-form .field{flex:1;background:var(--white);color:#999;font-size:8px;padding:4px 6px}
.news-form .go{background:var(--gold);width:22px}
.socials{display:flex;gap:5px;margin-top:10px}
.socials i{width:16px;height:16px;border-radius:50%;border:1px solid var(--text-muted)}
.contact-col{left:283px}
.links-col{left:438px}
.footer-brand{position:absolute;left:560px;top:40px;display:flex;align-items:center;gap:8px;font-size:12px;font-weight:700;color:var(--white)}
.footer-brand i{width:30px;height:30px;border-radius:50%;background:#2b2b2b}
.copyright{position:absolute;left:105px;top:150px;width:540px;border-top:1px solid #2c2c2c;padding-top:10px;text-align:center;font-size:7.5px;color:var(--text-muted)}
</style>
</head>
<body>
<header class="site-header">
  <div class="brand"><i class="brand-mark"></i>Orin Ventures Group</div>
  <div class="header-phone">
    <svg width="10" height="10" viewBox="0 0 24 24"><path fill="#e8b21c" d="M6.6 10.8a15 15 0 0 0 6.6 6.6l2.2-2.2c.3-.3.7-.4 1-.2 1.1.4 2.3.6 3.6.6.6 0 1 .4 1 1V20c0 .6-.4 1-1 1A17 17 0 0 1 3 4c0-.6.4-1 1-1h3.5c.6 0 1 .4 1 1 0 1.3.2 2.5.6 3.6.1.3 0 .7-.2 1z"/></svg>
    (0800) 415 2730
  </div>
  <nav class="main-nav"><span class="active">HOME</span><span>ABOUT</span><span>TEAM</span><span>SERVICES</span><span>PROJECT EXPERIENCE</span><span>CONTACT</span></nav>
</header>

<section class="hero" role="img" aria-label="Modern glass apartment buildings lit at dusk">
  <div class="watch-btn">
    <svg width="12" height="12" viewBox="0 0 12 12"><circle cx="6" cy="6" r="5.5" fill="none" stroke="#fff"/><path d="M4.8 3.6 8.4 6 4.8 8.4z" fill="#fff"/></svg>
    WATCH VIDEO
  </div>
</section>
<div class="gold-rule" style="top:350px"></div>

<section class="services-band">
  <article class="service-card" style="left:105px">
    <h3>Orin <span>Services</span></h3>
    <p>Direct funding for first mortgage, mezzanine and equity.</p>
    <span class="btn">Read more</span>
    <div class="service-photo" role="img" aria-label="Office building photo" style="background:linear-gradient(135deg,#c9d4dc,#7d8f9c)"></div>
  </article>
  <article class="service-card" style="left:292px">
    <h3>Orin <span>Team</span></h3>
    <p>Directors with over sixty years of property finance wisdom.</p>
    <span class="btn">Read more</span>
    <div class="service-photo" role="img" aria-label="Team at a meeting table" style="background:linear-gradient(135deg,#e2d8c6,#8a7b66)"></div>
  </article>
  <article class="service-card" style="left:480px">
    <h3>Orin <span>Project</span></h3>
    <p>Commercial and residential developments we have funded to date.</p>
    <span class="btn">Read more</span>
    <div class="service-photo" role="img" aria-label="Residential tower under blue sky" style="background:linear-gradient(135deg,#d8e4ee,#6d94b8)"></div>
  </article>
</section>

<section class="welcome">
  <div class="welcome-emblem"></div>
  <h2>Welcome to <span>Orin Ventures Group</span></h2>
  <div class="welcome-copy">
    <p>Orin Ventures Group is a private property finance company with capital to directly fund first mortgage, mezzanine and preferred equity financing. We also acquire performing, sub-performing and distressed debt across commercial and residential sectors.</p>
    <p>We are not finance brokers. We provide debt funding with fast turnaround times, solving funding problems for developers and businesses.</p>
  </div>
  <span class="btn">Read more</span>
</section>

<section class="highlights">
  <article class="info-card why-card">
    <h3>Why <span>Choose Us</span></h3>
    <ul class="why-list">
      <li><svg width="8" height="8" viewBox="0 0 8 8"><path d="M1 4.2 3 6.2 7 1.8" fill="none" stroke="#c8920c" stroke-width="1.4"/></svg>Fast turnaround times</li>
      <li><svg width="8" height="8" viewBox="0 0 8 8"><path d="M1 4.2 3 6.2 7 1.8" fill="none" stroke="#c8920c" stroke-width="1.4"/></svg>Direct debt funding</li>
      <li><svg width="8" height="8" viewBox="0 0 8 8"><path d="M1 4.2 3 6.2 7 1.8" fill="none" stroke="#c8920c" stroke-width="1.4"/></svg>Over sixty years wisdom</li>
      <li><svg width="8" height="8" viewBox="0 0 8 8"><path d="M1 4.2 3 6.2 7 1.8" fill="none" stroke="#c8920c" stroke-width="1.4"/></svg>Honest, clear terms</li>
      <li><svg width="8" height="8" viewBox="0 0 8 8"><path d="M1 4.2 3 6.2 7 1.8" fill="none" stroke="#c8920c" stroke-width="1.4"/></svg>Flexible loan structures</li>
      <li><svg width="8" height="8" viewBox="0 0 8 8"><path d="M1 4.2 3 6.2 7 1.8" fill="none" stroke="#c8920c" stroke-width="1.4"/></svg>First mortgage lending</li>
      <li><svg width="8" height="8" viewBox="0 0 8 8"><path d="M1 4.2 3 6.2 7 1.8" fill="none" stroke="#c8920c" stroke-width="1.4"/></svg>Mezzanine finance</li>
      <li><svg width="8" height="8" viewBox="0 0 8 8"><path d="M1 4.2 3 6.2 7 1.8" fill="none" stroke="#c8920c" stroke-width="1.4"/></svg>Distressed debt solutions</li>
    </ul>
    <div class="why-photo" role="img" aria-label="Smiling businessman in a blue shirt pointing to the list"></div>
  </article>
  <article class="info-card testimonial-card">
    <h3>Happy <span>Customers</span></h3>
    <p class="quote">Orin Ventures funded our development quickly and solved a problem the banks could not. Honest, expert and fast.</p>
    <p class="quote-name">Marla</p>
    <div class="dots"><i></i><i></i><i></i><i></i></div>
    <div class="customer-photo" role="img" aria-label="Portrait of a smiling female client"></div>
  </article>
</section>
<div class="gold-rule" style="top:1012px"></div>

<footer class="site-footer">
  <div class="footer-col news-col">
    <h4>Sign up for Newsletter</h4>
    <div class="news-form"><span class="field">Email Address</span><span class="go"></span></div>
    <div class="socials"><i></i><i></i><i></i><i></i></div>
  </div>
  <div class="footer-col contact-col">
    <h4>Contact Info</h4>
    <p>Orin Ventures Group<br>28 Kestrel Lane, Brookvale<br>Wellington 4021</p>
    <p style="margin-top:6px">T: (0800) 415 2730<br>E: hello@orinventures.example</p>
  </div>
  <div class="footer-col links-col">
    <h4>Quick Links</h4>
    <p>Home<br>About<br>Team<br>Services<br>Project Experience<br>Contact</p>
  </div>
  <div class="footer-brand"><i></i>Orin Ventures</div>
  <p class="copyright">Copyright © 2015 Orin Ventures Group. All Rights Reserved.</p>
</footer>
</body>
</html>
```